Recruitment Agency in Texas, needs a stand out header letter

Our colours are red and grey and can be found on our website
just my logo will be sufficient and address...

Target Market(s)

Engineering Manufacturing

Colors
0094D4
00A9DD
6FCCEA
C7EBF8
E9F6FB
EB3D1F
EC4F4E
F09395
F8D3D4
FCEDEE

Requirements
Must have
• use colors red and grey
Should not have
• Please use same colors and font as my logo. My website is kelbrinstaffing.com

```html
<!DOCTYPE html>
<html lang="en">
<head>
<meta charset="utf-8">
<title>KelbrinStaffing Letterhead</title>
<link href="https://fonts.googleapis.com/css2?family=Roboto:wght@300;400;700&family=Pinyon+Script&display=swap" rel="stylesheet">
<style>
  :root {
    --canvas: #e4e4e4;
    --paper: #f1f1f1;
    --paper-light: #f5f5f5;
    --brand-red: #e11f26;
    --ink: #2b2b2b;
    --ink-soft: #555555;
    --rule: #8a8a8a;
    --footer-dark: #2a292b;
    --white: #ffffff;
  }
  * { margin: 0; padding: 0; box-sizing: border-box; }
  html, body {
    width: 1200px; height: 1200px; overflow: hidden;
    background: var(--canvas);
    font-family: "Roboto", Arial, sans-serif;
  }
  .letterhead {
    position: absolute; left: 200px; top: 34px;
    width: 800px; height: 1131px;
    background: linear-gradient(135deg, var(--paper) 0%, var(--paper-light) 60%, var(--paper) 100%);
    box-shadow: 0 2px 14px rgba(0,0,0,0.12);
    overflow: hidden;
    color: var(--ink);
  }
  .brand-name {
    position: absolute; left: 54px; top: 60px;
    font-size: 34px; font-weight: 700; letter-spacing: -1px;
    color: var(--brand-red);
  }
  .office-contact {
    position: absolute; left: 549px; top: 38px;
    border-left: 1.5px solid var(--rule);
    padding-left: 13px;
    font-size: 13.2px; font-weight: 300; line-height: 16px;
    font-style: normal;
    color: var(--ink-soft);
  }
  .office-contact .contact-lines { margin-top: 6px; }
  .contact-item { display: flex; align-items: center; gap: 5px; }
  .contact-item svg { width: 10px; height: 10px; fill: var(--brand-red); }
  .letter-body {
    position: absolute; left: 85px; top: 266px; width: 630px;
    font-size: 13.2px; font-weight: 300; line-height: 18.8px;
    color: var(--ink);
  }
  .letter-date { margin-bottom: 18px; }
  .recipient { margin-bottom: 36px; }
  .salutation { margin-bottom: 19px; }
  .letter-body p.paragraph { text-align: justify; margin-bottom: 19px; }
  .closing { margin-top: 46px; }
  .signature {
    font-family: "Pinyon Script", cursive;
    font-size: 27px; line-height: 34px; margin-left: 4px; margin-top: 4px;
    color: var(--ink);
  }
  .footer-band {
    position: absolute; left: 0; bottom: 0; width: 800px; height: 64px;
    background: var(--footer-dark);
    border-top: 5px solid var(--brand-red);
  }
  .footer-url {
    position: absolute; right: 97px; top: 20px;
    font-size: 13px; font-weight: 300; color: var(--white);
  }
  .footer-url strong { font-weight: 700; }
</style>
</head>
<body>
  <main class="letterhead">
    <header>
      <div class="brand-name">KelbrinStaffing</div>
      <address class="office-contact">
        <div>Northside Branch Office</div>
        <div>48 Larkspur Plaza Suite 900</div>
        <div>Corvell, TX 76999</div>
        <div class="contact-lines">
          <div class="contact-item">
            <svg viewBox="0 0 10 10" aria-hidden="true"><path d="M2 0.5 L3.6 2.6 L2.7 3.6 C3.3 5 4.6 6.5 6.3 7.3 L7.3 6.3 L9.5 7.9 L8.3 9.5 C4.5 9.2 0.8 5.5 0.5 1.7 Z"/></svg>
            <span>(+1) 555-010-0148</span>
          </div>
          <div class="contact-item">
            <svg viewBox="0 0 10 10" aria-hidden="true"><path d="M0 2 H10 V8 H0 Z M0.6 2.4 L5 5.6 L9.4 2.4" stroke="#f1f1f1" stroke-width="0.8"/></svg>
            <span>info@kelbrinstaffing.com</span>
          </div>
        </div>
      </address>
    </header>

    <section class="letter-body">
      <div class="letter-date">01 January 2050</div>
      <div class="recipient">
        <div>Company (Pvt) Ltd.</div>
        <div>PO Box 3355 Mainville St</div>
        <div>Sample City Country 3355</div>
      </div>
      <div class="salutation">Dear Martin Ellwood,</div>
      <p class="paragraph">Lorem ipsum dolor sit amet, consectetuer adipiscing elit, sed diam nonummy nibh euismod tincidunt ut laoreet dolore magna aliquam erat volutpat. Ut wisi enim ad minim veniam, quis nostrud exerci tation ullamcorper suscipit lobortis nisl ut aliquip ex ea commodo consequat. Duis dolore te feugait nulla facilisi. Nam liber tempor cum soluta nobis eleifend option congue nihil imperdiet doming id quod mazim placerat facer possim assum. Lorem ipsum dolor sit amet, consectetuer adipiscing elit, sed diam nonummy nibh euismod tincidunt ut laoreet dolore magna aliquam erat volutpat. Ut wisi enim ad minim veniam, quis nostrud exerci tation ullamcorper suscipit lobortis nisl ut aliquip ex ea commodo consequat.</p>
      <p class="paragraph">Consectetuer adipiscing elit, sed diam nonummy nibh euismod tincidunt ut laoreet dolore magna aliquam erat volutpat. Ut wisi enim ad minim veniam, quis nostrud exerci tation ullamcorper suscipit lobortis nisl ut aliquip ex ea commodo consequat. Consectetuer adipiscing elit, sed diam nonummy nibh euismod tincidunt ut laoreet dolore magna aliquam erat volutpat. Ut wisi enim ad minim veniam, quis nostrud exerci tation ullamcorper suscipit lobortis nisl ut aliquip ex ea commodo consequat.</p>
      <p class="paragraph">Consectetuer adipiscing elit, sed diam nonummy nibh euismod tincidunt ut laoreet dolore magna aliquam erat volutpat. Ut wisi enim ad minim veniam, quis nostrud exerci tation ullamcorper suscipit lobortis nisl ut aliquip ex ea commodo consequat. Consectetuer adipiscing elit, sed diam nonummy nibh euismod tincidunt ut laoreet dolore magna aliquam erat volutpat. Ut wisi enim ad minim veniam, quis nostrud exerci tation ullamcorper suscipit lobortis nisl ut aliquip ex ea commodo consequat.</p>
      <div class="closing">Sincerely Yours</div>
      <div class="signature">Daniel Hart</div>
    </section>

    <footer class="footer-band">
      <div class="footer-url">www.<strong>kelbrinstaffing</strong>.com</div>
    </footer>
  </main>
</body>
</html>
```